Dental Practice Billboard Design

We are a newer dental practice in need of a simple but appealing billboard for our growing dental practice to attract new patients. The practice is owned by husband and wife dentists and is family friendly in a small town in Kentucky. We try to be very friendly and caring to our patients. Would prefer a blue background for the billboard and our tooth logo to be prominent. We are partial to the Patua One font used in the image below but please feel free to tweak it as you deem necessary. The shape of the uppercase D and lowercase g are why we like that font, so fonts with a similarly shaped “D” and “g” would work as well. Please include our phone number (606) 847-3962. Please see our website Harlowfamilydentistry.com for more info on the practice if needed. Thank you! Looking forward to seeing your creation.
Updates

The dimensions will be 12ft x 24ft (3.6576m x 7.3152m). Apologies for not including this in the original prompt. Thank you all for your submissions.

Industry/Entity Type

Dental

Font styles to use
Other font styles liked:
• Patua One

Colors
0054AA
0677BA
7BADD7
CADEEF
E8F1F8
0094D4
00A9DD
6FCCEA
C7EBF8
E9F6FB
00AB8E
00BBA5
67D7C9
C6EFE9
E9F9F6
59FF00
82FF00
B8FF75
E3FFCB
F4FFEA

Requirements
Must have
• Phone number, website, Logo, Practice name “Harlow Family Dentistry”
Should not have
• A tagline or slogan

```html
<!DOCTYPE html>
<html lang="en">
<head>
<meta charset="utf-8">
<title>Harlow Family Dentistry Billboard</title>
<link rel="stylesheet" href="https://fonts.googleapis.com/css2?family=Fira+Sans:wght@600;700&display=swap">
<style>
  :root {
    --page-bg: #f2f2f2;
    --brand-blue: #2458a8;
    --brand-teal: #158a8c;
    --brand-green: #1fae55;
    --pill-green: #27b24e;
    --logo-blue: #1d4fa3;
    --white: #ffffff;
    --photo-light: #f6dfe4;
    --photo-mid: #e8c3cc;
    --photo-accent: #b8b2e6;
  }
  * { box-sizing: border-box; margin: 0; padding: 0; }
  html, body {
    width: 1200px;
    height: 1200px;
    overflow: hidden;
    background: var(--page-bg);
    font-family: "Fira Sans", Arial, sans-serif;
  }
  .billboard {
    position: absolute;
    left: 50px;
    top: 395px;
    width: 1100px;
    height: 410px;
    overflow: hidden;
    background: linear-gradient(115deg, var(--brand-blue) 0%, var(--brand-teal) 52%, var(--brand-green) 100%);
  }
  .photo-stripes {
    position: absolute;
    inset: 0;
    width: 1100px;
    height: 410px;
  }
  .logo-panel {
    position: absolute;
    left: 59px;
    top: 47px;
    width: 288px;
    height: 120px;
    background: var(--white);
    display: flex;
    align-items: center;
    gap: 16px;
    padding: 0 18px;
  }
  .logo-dot {
    flex: none;
    width: 54px;
    height: 54px;
    border-radius: 50%;
    background: var(--logo-blue);
  }
  .practice-name {
    color: var(--logo-blue);
    font-weight: 700;
    font-size: 27px;
    line-height: 1.1;
  }
  .website {
    position: absolute;
    left: 59px;
    top: 180px;
    color: var(--white);
    font-weight: 600;
    font-size: 20px;
  }
  .phone-pill {
    position: absolute;
    left: 0;
    top: 288px;
    width: 440px;
    height: 63px;
    background: var(--pill-green);
    border-radius: 0 32px 32px 0;
    display: flex;
    align-items: center;
    gap: 12px;
    padding-left: 56px;
    color: var(--white);
    font-weight: 700;
    font-size: 35px;
  }
  .phone-icon { width: 34px; height: 34px; flex: none; }
</style>
</head>
<body>
  <div class="billboard">
    <svg class="photo-stripes" viewBox="0 0 1100 410" role="img" aria-label="Photo of a dentist in gloves holding a dental tool and a tooth model, shown through diagonal stripes">
      <defs>
        <linearGradient id="photoTone" x1="0" y1="0" x2="1" y2="0">
          <stop offset="0" stop-color="var(--photo-mid)"/>
          <stop offset="0.45" stop-color="var(--photo-light)"/>
          <stop offset="0.7" stop-color="var(--photo-accent)"/>
          <stop offset="1" stop-color="var(--photo-light)"/>
        </linearGradient>
      </defs>
      <g class="faint-stripes" fill="#ffffff" fill-opacity="0.18">
        <rect x="0" y="-37" width="700" height="74" rx="37" transform="translate(483 244) rotate(-42)"/>
        <rect x="0" y="-37" width="700" height="74" rx="37" transform="translate(589 291) rotate(-42)"/>
        <rect x="0" y="-37" width="700" height="74" rx="37" transform="translate(636 364) rotate(-42)"/>
        <rect x="0" y="-37" width="700" height="74" rx="37" transform="translate(729 391) rotate(-42)"/>
      </g>
      <g class="photo-bands" fill="url(#photoTone)">
        <rect x="0" y="-40" width="700" height="80" rx="40" transform="translate(496 164) rotate(-42)"/>
        <rect x="0" y="-40" width="700" height="80" rx="40" transform="translate(629 171) rotate(-42)"/>
        <rect x="0" y="-42" width="700" height="84" rx="42" transform="translate(709 222) rotate(-42)"/>
        <rect x="0" y="-44" width="700" height="88" rx="44" transform="translate(796 311) rotate(-42)"/>
      </g>
    </svg>

    <div class="logo-panel">
      <span class="logo-dot"></span>
      <span class="practice-name">Harlow Family Dentistry</span>
    </div>

    <p class="website">Harlowfamilydentistry.com</p>

    <div class="phone-pill">
      <svg class="phone-icon" viewBox="0 0 34 34" aria-hidden="true">
        <circle cx="17" cy="17" r="14.5" fill="none" stroke="#ffffff" stroke-width="3"/>
        <path d="M12 9.5l3 3.2-1.8 2.3c1.2 2.3 2.9 4 5.2 5.2l2.3-1.8 3.2 3-1.7 2.6c-5.6-.6-11.4-6.4-12-12z" fill="#ffffff"/>
      </svg>
      <span class="phone-number">(606) 847-3962</span>
    </div>
  </div>
</body>
</html>
```